Business card for femtech company

Nothing too elaborate but elegant and geared towards the mother and baby market. Prefer full-bleed with logo (attached) rear.

```html
<!DOCTYPE html>
<html lang="en">
<head>
<meta charset="utf-8">
<title>nuvella business card</title>
<link href="https://fonts.googleapis.com/css2?family=Poppins:wght@400;500&display=swap" rel="stylesheet">
<style>
  :root {
    --teal: #5bc3b8;
    --teal-soft: #e9f6f4;
    --teal-faint: #6fcbc1;
    --ink: #4a4a4a;
    --grey: #9a9a9a;
    --paper: #ffffff;
    --backdrop: #bdbdbd;
  }
  * { box-sizing: border-box; margin: 0; padding: 0; }
  html, body {
    width: 1200px; height: 900px; overflow: hidden;
    background: var(--backdrop);
    font-family: "Poppins", sans-serif;
  }
  .sheet {
    width: 1200px; height: 900px;
    display: flex; flex-direction: column; align-items: center; justify-content: center;
    gap: 44px;
  }
  .card {
    position: relative;
    width: 700px; height: 400px;
    border-radius: 34px;
    overflow: hidden;
  }
  .card-front { background: var(--teal); }
  .card-back { background: var(--paper); }

  .bg-circle { position: absolute; border-radius: 50%; }
  .card-front .bg-circle {
    width: 360px; height: 360px; right: 40px; top: -20px;
    background: var(--teal-faint);
  }
  .card-back .bg-circle {
    width: 380px; height: 380px; right: -30px; top: -60px;
    background: var(--teal-soft);
  }

  .brand {
    position: absolute;
    display: flex; align-items: center; gap: 18px;
    font-weight: 500; letter-spacing: 1px;
  }
  .brand-dot { border-radius: 50%; flex: none; }
  .card-front .brand {
    left: 50%; top: 50%; transform: translate(-50%, -50%);
    color: var(--paper); font-size: 84px;
  }
  .card-front .brand-dot { width: 64px; height: 64px; background: var(--paper); }
  .card-back .brand {
    left: 56px; top: 62px; color: var(--grey); font-size: 62px;
  }
  .card-back .brand-dot { width: 52px; height: 52px; background: var(--teal); }

  .person { position: absolute; left: 62px; top: 208px; }
  .person-name { color: var(--teal); font-size: 30px; font-weight: 500; line-height: 1.1; }
  .person-role { color: var(--ink); font-size: 18px; line-height: 1.2; }

  .contacts {
    position: absolute; left: 62px; top: 290px;
    list-style: none; color: var(--ink); font-size: 17px; line-height: 27px;
  }
  .contacts li { display: flex; align-items: center; gap: 10px; }
  .contacts svg { width: 18px; height: 18px; flex: none; }

  .address {
    position: absolute; right: 46px; top: 205px;
    color: var(--ink); font-size: 16px; line-height: 24px; text-align: left;
  }
</style>
</head>
<body>
<main class="sheet">
  <section class="card card-front" aria-label="Card front">
    <div class="bg-circle"></div>
    <div class="brand"><span class="brand-dot"></span>nuvella</div>
  </section>

  <section class="card card-back" aria-label="Card back">
    <div class="bg-circle"></div>
    <div class="brand"><span class="brand-dot"></span>nuvella</div>

    <div class="person">
      <p class="person-name">Maeve Carrick</p>
      <p class="person-role">CEO</p>
    </div>

    <ul class="contacts">
      <li>
        <svg viewBox="0 0 24 24" aria-hidden="true"><path fill="#5bc3b8" d="M6.6 10.8a15.1 15.1 0 0 0 6.6 6.6l2.2-2.2c.3-.3.7-.4 1-.2 1.1.4 2.3.6 3.6.6.6 0 1 .4 1 1V20c0 .6-.4 1-1 1A17 17 0 0 1 3 4c0-.6.4-1 1-1h3.5c.6 0 1 .4 1 1 0 1.3.2 2.5.6 3.6.1.3 0 .7-.2 1z"/></svg>
        +353 86 555 0142
      </li>
      <li>
        <svg viewBox="0 0 24 24" aria-hidden="true"><rect x="2" y="5" width="20" height="14" rx="1.5" fill="#5bc3b8"/><path d="M3 6.5l9 6.5 9-6.5" fill="none" stroke="#fff" stroke-width="1.6"/></svg>
        maeve@nuvella.com
      </li>
      <li>
        <svg viewBox="0 0 24 24" aria-hidden="true"><circle cx="12" cy="12" r="9.5" fill="none" stroke="#5bc3b8" stroke-width="2"/><ellipse cx="12" cy="12" rx="4" ry="9.5" fill="none" stroke="#5bc3b8" stroke-width="1.6"/><path d="M2.5 12h19M4 7h16M4 17h16" stroke="#5bc3b8" stroke-width="1.4"/></svg>
        www.nuvellababy.com
      </li>
    </ul>

    <p class="address">Unit 4 Harbour Works, Lisgarran<br>Marlow Bay, M42 R2P7 Ireland</p>
  </section>
</main>
</body>
</html>
```